Entertainer/Dancer Business Cards

Devon Marsh is an up and coming entertainer from Baltimore, Maryland currently relocating to Los Angeles, California for a dance opportunity at the renowned Ruthie Calder Dance Studio.
This young man needs to promote himself and his skills in a populous and competitive city.
Hopefully, this card will set him apart from the tons of entertainers in L.A.
It will passed out to fellow entertainers, agents, and random people looking for talent.

I have uploaded an image of the dancer, it is not necessary to use this image; however it is in PSD format if one should decide to incorporate it somehow and would like to make changes.

Industry/Entity Type

Business

Contact Information for Business Card

Devon Marsh
(line 1) Dancer Choreographer Instructor Singer/Songwriter
(line 2) Ballet-Modern-Urban
devonmarsh00@fernpost.com
410-582-7146

Requirements
Nice to have

• Open to an all typography card.
Should not have
• No logo; just name: Devon Marsh
Devon is a guy (in case you were wondering :D )
Please no ballet/pointe shoes in design

```html
<!DOCTYPE html>
<html lang="en">
<head>
<meta charset="utf-8">
<title>Devon Marsh – Business Card</title>
<link href="https://fonts.googleapis.com/css2?family=Titillium+Web:wght@400;600;700&display=swap" rel="stylesheet">
<style>
  :root {
    --page: #ffffff;
    --ink: #ffffff;
    --wood-deep: #2f3552;
    --wood-violet: #5c4d72;
    --wood-plum: #6b5066;
    --wood-brown: #74524c;
    --wood-slate: #47506e;
  }
  html, body {
    margin: 0;
    padding: 0;
    width: 1200px;
    height: 704px;
    overflow: hidden;
    background: var(--page);
  }
  .canvas {
    position: relative;
    width: 1200px;
    height: 704px;
    background: var(--page);
  }
  .card {
    position: absolute;
    left: 25px;
    top: 25px;
    width: 1150px;
    height: 652px;
    overflow: hidden;
    font-family: "Titillium Web", sans-serif;
    color: var(--ink);
  }
  .card__backdrop {
    position: absolute;
    inset: 0;
    background:
      radial-gradient(ellipse at 75% 20%, rgba(130, 80, 70, 0.55), transparent 60%),
      radial-gradient(ellipse at 20% 80%, rgba(60, 70, 120, 0.45), transparent 60%),
      linear-gradient(160deg, var(--wood-plum) 0%, var(--wood-violet) 35%, var(--wood-slate) 65%, var(--wood-brown) 100%);
  }
  .card__backdrop::after {
    content: "";
    position: absolute;
    inset: 0;
    background: radial-gradient(ellipse at 50% 50%, transparent 40%, rgba(30, 30, 50, 0.35) 100%);
  }
  .card__name {
    position: absolute;
    left: 0;
    right: 0;
    top: 186px;
    margin: 0;
    text-align: center;
    font-weight: 700;
    font-size: 122px;
    line-height: 1;
    letter-spacing: 4px;
    word-spacing: 18px;
    text-transform: uppercase;
  }
  .card__rule {
    position: absolute;
    left: 146px;
    top: 365px;
    width: 858px;
    height: 10px;
  }
  .card__roles {
    position: absolute;
    left: 0;
    right: 0;
    top: 400px;
    margin: 0;
    text-align: center;
    font-weight: 400;
    font-size: 33px;
    line-height: 43px;
  }
  .card__contact {
    position: absolute;
    left: 0;
    right: 0;
    top: 502px;
    margin: 0;
    text-align: center;
    font-weight: 600;
    font-size: 33px;
    line-height: 40px;
    letter-spacing: 0.5px;
  }
  .card__divider {
    display: inline-block;
    margin: 0 26px 0 22px;
  }
</style>
</head>
<body>
<main class="canvas">
  <section class="card">
    <div class="card__backdrop" role="img" aria-label="Photo of weathered wooden dance-floor boards in perspective, in purple and brown tones"></div>

    <h1 class="card__name">Devon Marsh</h1>

    <svg class="card__rule" viewBox="0 0 858 10" aria-hidden="true">
      <defs>
        <pattern id="wave" width="16" height="10" patternUnits="userSpaceOnUse">
          <path d="M0 5 Q4 1 8 5 T16 5" fill="none" stroke="#ffffff" stroke-width="1.6"/>
        </pattern>
      </defs>
      <rect x="0" y="0" width="858" height="10" fill="url(#wave)"/>
    </svg>

    <p class="card__roles">
      Dancer Choreographer Instructor<br>
      Singer/Songwriter Ballet-Modern-Urban
    </p>

    <p class="card__contact">
      <span class="card__email">devonmarsh00@fernpost.com</span><span class="card__divider">|</span><span class="card__phone">410-582-7146</span>
    </p>
  </section>
</main>
</body>
</html>
```